Maplewood Farms - business cards
Business Card
Project: Maplewood Farms - business cards
Maplewood Farms - business cards - Agriculture
Creative Brief
Use same font as used in my logo
Glen Patters
38672 Red Falcon Lane Cheney, WA 99004
gpatters@ironvale-partners.example
Can I see the design for a one sided card vs a 2 sided card? I want to send to the printer to see how much more it costs for 2 sided.
we might just do one sided; for a two sided card, just the logo

```html
<!DOCTYPE html>
<html lang="en">
<head>
<meta charset="utf-8">
<title>Maplewood Farms – Business Card</title>
<link rel="stylesheet" href="https://fonts.googleapis.com/css2?family=Noto+Serif:wght@400;700&display=swap">
<style>
  :root {
    --backdrop: #5e5e60;
    --card-white: #ffffff;
    --harvest-gold: #ecb32e;
    --deep-gold: #b5861b;
    --ink: #4a4a4a;
    --rule: #c9c9c9;
  }
  * { box-sizing: border-box; margin: 0; padding: 0; }
  html, body {
    width: 1200px;
    height: 780px;
    overflow: hidden;
    background: var(--backdrop);
  }
  .canvas {
    position: relative;
    width: 1200px;
    height: 780px;
  }
  .business-card {
    position: absolute;
    left: 60px;
    top: 81px;
    width: 1080px;
    height: 618px;
    border-radius: 36px;
    background: var(--card-white);
    overflow: hidden;
    box-shadow: 0 10px 30px rgba(0,0,0,0.35);
    font-family: "Noto Serif", Georgia, serif;
  }
  .header-band {
    position: absolute;
    inset: 0;
    width: 1080px;
    height: 618px;
  }
  .holder-name {
    position: absolute;
    right: 70px;
    top: 40px;
    color: var(--card-white);
    font-weight: 700;
    font-size: 30px;
    letter-spacing: 0.3px;
  }
  .brand-mark {
    position: absolute;
    left: 56px;
    top: 396px;
    width: 380px;
    display: flex;
    align-items: center;
    gap: 12px;
  }
  .brand-dot {
    width: 20px;
    height: 20px;
    border-radius: 50%;
    background: var(--harvest-gold);
    flex: none;
  }
  .brand-name {
    color: var(--harvest-gold);
    font-weight: 700;
    font-size: 34px;
    white-space: nowrap;
  }
  .divider {
    position: absolute;
    left: 470px;
    top: 300px;
    width: 2px;
    height: 190px;
    background: var(--rule);
  }
  .contact-block {
    position: absolute;
    left: 492px;
    top: 305px;
    color: var(--ink);
    font-size: 19px;
    line-height: 1.45;
    font-style: normal;
  }
  .postal-address { margin-bottom: 26px; }
  .contact-list { list-style: none; }
  .contact-item {
    display: flex;
    align-items: center;
    gap: 10px;
    height: 32px;
  }
  .contact-icon { width: 18px; height: 18px; flex: none; }
</style>
</head>
<body>
<main class="canvas">
  <article class="business-card">
    <svg class="header-band" viewBox="0 0 1080 618" aria-hidden="true">
      <path d="M0,0 H1080 V150 C760,148 360,200 0,318 Z" fill="var(--harvest-gold)"/>
      <path d="M0,318 C360,200 760,148 1080,150 V166 C760,166 360,218 0,346 Z" fill="var(--card-white)"/>
      <path d="M0,346 C360,218 760,166 1080,166 V178 C760,180 380,230 0,372 Z" fill="var(--deep-gold)"/>
    </svg>

    <h1 class="holder-name">Glen Patters</h1>

    <div class="brand-mark">
      <span class="brand-dot"></span>
      <span class="brand-name">Maplewood Farms</span>
    </div>

    <div class="divider"></div>

    <address class="contact-block">
      <p class="postal-address">38672 Red Falcon Lane<br>Cheney, WA 99004</p>
      <ul class="contact-list">
        <li class="contact-item">
          <svg class="contact-icon" viewBox="0 0 18 18" aria-label="Phone"><rect x="5" y="1" width="8" height="16" rx="2" fill="var(--harvest-gold)"/><rect x="6.5" y="3" width="5" height="9" fill="#fff"/></svg>
          <span>509.555.0147</span>
        </li>
        <li class="contact-item">
          <svg class="contact-icon" viewBox="0 0 18 18" aria-label="Email"><rect x="1" y="4" width="16" height="11" rx="1.5" fill="var(--harvest-gold)"/><path d="M1.5,5 L9,11 L16.5,5" fill="none" stroke="#fff" stroke-width="1.4"/></svg>
          <span>gpatters@ironvale-partners.example</span>
        </li>
        <li class="contact-item">
          <svg class="contact-icon" viewBox="0 0 18 18" aria-label="Website"><circle cx="9" cy="9" r="7.5" fill="var(--harvest-gold)"/><ellipse cx="9" cy="9" rx="3" ry="7.5" fill="none" stroke="#fff" stroke-width="1.2"/><path d="M1.5,9 H16.5" stroke="#fff" stroke-width="1.2"/></svg>
          <span>www.ironvale-partners.example</span>
        </li>
      </ul>
    </address>
  </article>
</main>
</body>
</html>
```